Flyer for local business that installs fences and sells fence materials

We recently began selling fence materials, in addition to also doing fence installations. We need a flyer that displays our business information and photos of our work, as well as a flyer that shows customers they have the option to buy materials only also.

If they are looking to build a fence - we can help by installing it, or if they want to install themselves, they can buy the materials only from us too. We provide a lifetime warranty on all materials and installations. More information about the company is here: www.BrambleRailWorks.com

Its important to have the company logo, phone number, email and business hours listed (Monday - Thursday 9AM - 3PM, Friday 9AM - 1PM).

It is also important to show the fence material types we offer:
Wood, Chainlink, Vinyl and Aluminum
Updates

Updated with more photos and url to website www.bramblerailworks.com for details

Target Market(s)

Residential Homeowners

Industry/Entity Type

Construction

Font styles to use
Sans Serif
Other font styles liked:
• Arial

Colors
0054AA
0677BA
7BADD7
CADEEF
E8F1F8

Requirements
Must have
• Photos of the fencing we offer
Nice to have
• A way to explain to customers they can hire us to install, or just buy the materials from us
Should not have
• Too many colors or too many words

```html
<!DOCTYPE html>
<html lang="en">
<head>
<meta charset="utf-8">
<title>Bramble Rail Works Flyer</title>
<link href="https://fonts.googleapis.com/css2?family=Arimo:wght@400;700&display=swap" rel="stylesheet">
<style>
  :root {
    --page-bg: #e4e4e4;
    --panel-dark: #2b2b2c;
    --panel-mid: #4a4a4b;
    --ink: #111111;
    --ink-soft: #333333;
    --brand-blue: #3f8fd6;
    --band-blue-dark: #16365c;
    --band-blue: #2e5f97;
    --soft-grey: #e3e5e9;
    --free-blue: #1aa3ff;
    --white: #ffffff;
  }
  * { box-sizing: border-box; margin: 0; padding: 0; }
  html, body {
    width: 1200px; height: 848px; overflow: hidden;
    background: var(--page-bg);
    font-family: "Arimo", Arial, sans-serif;
  }
  .flyer {
    position: absolute; left: 330px; top: 74px;
    width: 540px; height: 700px;
    background: var(--white);
    box-shadow: 0 3px 10px rgba(0,0,0,.35);
    overflow: hidden;
  }
  .gallery {
    position: absolute; left: 0; top: 0; width: 268px; height: 100%;
    background: linear-gradient(180deg, var(--panel-mid) 0%, var(--panel-dark) 40%, var(--panel-dark) 100%);
  }
  .photo {
    position: absolute; left: 22px; width: 230px; height: 116px;
    border: 3px solid var(--white);
    box-shadow: 4px 4px 6px rgba(0,0,0,.5);
  }
  .photo-wood { top: 40px; background: linear-gradient(100deg, #6a4a2c 0%, #d8b38a 45%, #e6c59f 70%, #5d7fb8 100%); }
  .photo-vinyl { top: 173px; background: linear-gradient(180deg, #5b7fb6 0%, #9fb3cf 30%, #eceae6 45%, #d9d7d2 75%, #7a5b3d 100%); }
  .photo-chain { top: 306px; background: linear-gradient(180deg, #4d5a3c 0%, #8a8f86 40%, #a89277 75%, #6a543a 100%); }
  .photo-stock { top: 439px; background: linear-gradient(180deg, #2f4a28 0%, #b9b0a0 35%, #d6c7ae 70%, #cfc5b6 100%); }
  .materials {
    position: absolute; left: 0; top: 580px; width: 268px;
    color: var(--white); font-size: 13px; line-height: 16px;
  }
  .materials-highlight {
    padding: 2px 0 2px 20px;
    background: linear-gradient(90deg, #1f4d80 0%, rgba(31,77,128,0) 90%);
  }
  .materials-note { padding: 2px 0 0 20px; }
  .info { position: absolute; left: 268px; top: 0; width: 272px; height: 100%; }
  .shapes { position: absolute; left: 0; top: 0; }
  .brand { position: absolute; left: 20px; top: 48px; display: flex; gap: 8px; align-items: flex-start; }
  .brand-mark { width: 48px; height: 56px; background: #5a3a22; margin-top: 4px; }
  .brand-name { color: var(--brand-blue); font-weight: 700; font-size: 19px; line-height: 21px; }
  .brand-phone { color: var(--ink); font-weight: 700; font-size: 19px; line-height: 22px; }
  .brand-tagline { color: var(--ink); font-weight: 700; font-size: 7px; margin-top: 4px; }
  .perks {
    position: absolute; left: 20px; top: 128px; list-style: none;
    color: var(--ink); font-weight: 700; font-size: 11px; line-height: 15.2px;
  }
  .headline { position: absolute; left: 20px; top: 322px; color: var(--white); }
  .headline h1 { font-size: 21px; font-weight: 700; letter-spacing: .3px; }
  .headline p { font-size: 18px; line-height: 19px; margin-top: 4px; letter-spacing: -.3px; }
  .estimate-badge {
    position: absolute; left: 134px; top: 398px; width: 112px; height: 112px;
    border-radius: 50%; background: #000;
    color: var(--white); text-align: center;
    display: flex; flex-direction: column; justify-content: center;
    font-size: 18px; line-height: 21px;
  }
  .estimate-badge strong { color: var(--free-blue); font-weight: 700; }
  .contact {
    position: absolute; left: 20px; top: 520px; width: 245px;
    color: var(--ink-soft); font-size: 10px; line-height: 16px;
  }
  .hours {
    position: absolute; left: 20px; top: 600px;
    color: var(--ink-soft); font-size: 13px; line-height: 21px; letter-spacing: -.2px;
  }
  .hours b { color: var(--ink); }
  .social-dot {
    position: absolute; left: 225px; top: 638px; width: 22px; height: 22px;
    border-radius: 50%; background: #1877f2;
  }
</style>
</head>
<body>
  <article class="flyer">
    <section class="gallery">
      <div class="photo photo-wood" role="img" aria-label="Photo of an installed natural wood privacy fence"></div>
      <div class="photo photo-vinyl" role="img" aria-label="Photo of a white vinyl privacy fence behind houses"></div>
      <div class="photo photo-chain" role="img" aria-label="Photo of a chainlink fence in a grassy yard"></div>
      <div class="photo photo-stock" role="img" aria-label="Photo of wrapped pallets of fence materials"></div>
      <div class="materials">
        <p class="materials-highlight">We offer Wood, Chainlink, Vinyl<br>and Aluminum materials</p>
        <p class="materials-note">Beautiful professionally installed fences<br>at affordable prices</p>
      </div>
    </section>

    <section class="info">
      <svg class="shapes" width="272" height="700" viewBox="0 0 272 700" aria-hidden="true">
        <defs>
          <linearGradient id="bandFill" x1="0" y1="0" x2="0" y2="1">
            <stop offset="0" stop-color="var(--band-blue-dark)"/>
            <stop offset="1" stop-color="var(--band-blue)"/>
          </linearGradient>
        </defs>
        <polygon points="272,158 272,320 60,272 110,262" fill="var(--soft-grey)"/>
        <polygon points="0,258 272,318 272,482 0,404" fill="url(#bandFill)"/>
        <polygon points="0,404 272,482 0,520" fill="var(--soft-grey)"/>
      </svg>

      <div class="brand">
        <div class="brand-mark"></div>
        <div>
          <div class="brand-name">Bramble Rail Works</div>
          <div class="brand-phone">555-014-2290</div>
          <div class="brand-tagline">"Because Good Fences Make Good Neighbors"</div>
        </div>
      </div>

      <ul class="perks">
        <li>FREE ESTIMATES</li>
        <li>PROFESSIONAL INSTALLATION</li>
        <li>CONCRETE IN EVERY POST</li>
        <li>HOA SUBMISSION ASSISTANCE</li>
        <li>LIFETIME WORKMANSHIP WARRANTY</li>
        <li>EXPERIENCED INSTALLATION TEAM</li>
        <li>QUALITY WORKMANSHIP AND MATERIALS</li>
        <li>FREE GATE ADJUSTMENTS FOR LIFE</li>
      </ul>

      <div class="headline">
        <h1>WE BUILD FENCES</h1>
        <p>And we would love<br>to build your fence too!</p>
      </div>

      <div class="estimate-badge">
        <span>Estimates</span>
        <span>are always</span>
        <strong>FREE</strong>
      </div>

      <p class="contact">
        Call, email, or mesage us online to schedule<br>
        an in-person estimate.<br>
        If you know your measurements or have a lot survey<br>
        email or call us for a virtual estimate.
      </p>

      <p class="hours">
        MONDAY TO THURSDAY <b>9AM - 3PM</b><br>
        FRIDAY <b>9AM - 1PM</b>
      </p>

      <div class="social-dot" aria-label="Social media page"></div>
    </section>
  </article>
</body>
</html>
```